Wanderlark Gin - Bottle Label for a craft Gin about to be launched on the world from New Zealand

We are a start up craft distillery in New Zealand. We have developed a wonderful Gin using our own grain spirit and both traditional and New Zealand native botanicals (Manuka to be specific), chosen our bottle and the name "Wanderlark" and done a bit of amateur label design and now we are looking for someone to make it great.

Feel free to change up our amateur concept but give us something that will pop from the back bar and scream authenticity, craft and individuality.

The attached files give you the specifications of the bottle, our current concept for a Wanderlark label and an earlier concept drawing that gives an idea of where we are thinking the two labels should go on the front of the bottle.

Thanks, we look forward to your ideas!!

Target Market(s)

High end and craft Gin drinkers. Hipsters and cocktail barflys and their bar tenders and bar owners

Requirements
Must have
• Attractive individuality
Nice to have
• Coolness
Should not have
• Uncoolness

```html
<!DOCTYPE html>
<html lang="en">
<head>
<meta charset="utf-8">
<title>Wanderlark Gin – Recipe #3 Label</title>
<link rel="stylesheet" href="https://fonts.googleapis.com/css2?family=Oranienbaum&family=Cormorant+Garamond:ital,wght@0,500;0,600;1,400&display=swap">
<style>
  :root {
    --backdrop: #f4f4f2;
    --board: #e3e3e1;
    --board-light: #f0f0ee;
    --gold: #b8955a;
    --gold-dark: #9c7a44;
    --ink: #2a2a2a;
    --rule-grey: #a9a9a9;
    --leaf-green: #9dbf7e;
    --leaf-pale: #e4ecd9;
  }
  * { box-sizing: border-box; margin: 0; padding: 0; }
  html, body {
    width: 1200px; height: 2965px; overflow: hidden;
    background: var(--backdrop);
  }
  .label {
    position: absolute; left: 100px; top: 222px;
    width: 1000px; height: 2520px;
  }
  .panel-brand {
    position: absolute; left: 0; top: 0; width: 1000px; height: 940px;
    background: linear-gradient(90deg, var(--board), var(--board-light) 45%, var(--board));
    border: 14px solid var(--gold);
    border-radius: 40px 40px 0 0;
    text-align: center;
  }
  .brand-name {
    position: absolute; left: 60px; right: 60px; top: 320px;
    font-family: "Oranienbaum", serif; font-weight: 400;
    font-size: 136px; line-height: 1; letter-spacing: 0;
    color: var(--ink); text-transform: uppercase;
    white-space: nowrap;
  }
  .brand-origin {
    position: absolute; left: 0; right: 0; top: 500px;
    font-family: "Cormorant Garamond", serif; font-weight: 500;
    font-size: 40px; letter-spacing: 3px;
    color: var(--gold); text-transform: uppercase;
  }
  .spirit-row {
    position: absolute; left: 100px; right: 100px; top: 650px;
    height: 170px; display: flex; align-items: center; justify-content: center; gap: 30px;
  }
  .spirit-rule { flex: 1; height: 60px; }
  .spirit-name {
    font-family: "Oranienbaum", serif; font-size: 140px; line-height: 1;
    color: var(--ink);
  }
  .botanical-art {
    position: absolute; left: 0; top: 940px; width: 1000px; height: 770px;
    background: radial-gradient(ellipse at 50% 50%, var(--leaf-pale), #cfdcbd 60%, var(--leaf-green));
  }
  .panel-recipe {
    position: absolute; left: 0; top: 1710px; width: 1000px; height: 810px;
    background: linear-gradient(90deg, var(--board), var(--board-light) 45%, var(--board));
    border: 14px solid var(--gold); border-top-width: 8px;
    border-radius: 0 0 40px 40px;
    text-align: center;
  }
  .recipe-title {
    margin-top: 24px;
    font-family: "Cormorant Garamond", serif; font-weight: 600;
    font-size: 72px; color: var(--gold-dark);
  }
  .recipe-divider { display: block; margin: 6px auto 0; width: 900px; height: 24px; }
  .recipe-notes {
    margin: 20px auto 0; width: 760px;
    font-family: "Cormorant Garamond", serif; font-style: italic; font-weight: 400;
    font-size: 46px; line-height: 86px; color: var(--ink);
  }
  .recipe-footer {
    position: absolute; left: 40px; right: 40px; bottom: 20px;
    border-top: 3px solid var(--gold);
    padding-top: 16px;
    display: flex; justify-content: space-between;
    font-family: "Cormorant Garamond", serif; font-weight: 500;
    font-size: 34px; color: var(--ink);
  }
</style>
</head>
<body>
  <main class="label">
    <section class="panel-brand">
      <h1 class="brand-name">Wanderlark</h1>
      <p class="brand-origin">New Zealand Small Batch</p>
      <div class="spirit-row">
        <svg class="spirit-rule" viewBox="0 0 300 60" preserveAspectRatio="none" aria-hidden="true">
          <g stroke="var(--rule-grey)" stroke-width="2">
            <line x1="0" y1="10" x2="300" y2="10"/><line x1="0" y1="20" x2="300" y2="20"/>
            <line x1="0" y1="40" x2="300" y2="40"/><line x1="0" y1="50" x2="300" y2="50"/>
          </g>
          <line x1="0" y1="30" x2="300" y2="30" stroke="var(--gold)" stroke-width="5"/>
        </svg>
        <span class="spirit-name">GIN</span>
        <svg class="spirit-rule" viewBox="0 0 300 60" preserveAspectRatio="none" aria-hidden="true">
          <g stroke="var(--rule-grey)" stroke-width="2">
            <line x1="0" y1="10" x2="300" y2="10"/><line x1="0" y1="20" x2="300" y2="20"/>
            <line x1="0" y1="40" x2="300" y2="40"/><line x1="0" y1="50" x2="300" y2="50"/>
          </g>
          <line x1="0" y1="30" x2="300" y2="30" stroke="var(--gold)" stroke-width="5"/>
        </svg>
      </div>
    </section>

    <div class="botanical-art" role="img" aria-label="Illustration of juniper sprigs with dark blue juniper berries"></div>

    <section class="panel-recipe">
      <h2 class="recipe-title">Recipe#3</h2>
      <svg class="recipe-divider" viewBox="0 0 900 24" aria-hidden="true">
        <line x1="10" y1="12" x2="890" y2="12" stroke="var(--gold)" stroke-width="3"/>
        <polygon points="0,12 14,4 14,20" fill="var(--gold)"/>
        <polygon points="900,12 886,4 886,20" fill="var(--gold)"/>
      </svg>
      <p class="recipe-notes">A classically inspired Gin with a New Zealand twist. Distilled in-house starting with Canterbury grain and finished with 11 botanicals including a generous helping of East Coast Manuka Berries, Gisborne Citrus and Otago Lavender</p>
      <div class="recipe-footer">
        <span class="volume">500ml</span>
        <span class="abv">42% Alc. by Vol</span>
      </div>
    </section>
  </main>
</body>
</html>
```